Postcard Design - Car buying service

I am launching a car buying service in Florida. We help people find the car they want, and negotiate the price down for them and ensure they aren't being taken advantage of by the dealership.

I am in need of a postcard that we can use to leave on people's cars, in store counters etc. This should draw people to our website and give a brief description of what we do.

I have attached our logo that should be on the postcard as well.

Target Market(s)

A majority will be women between 18 and 55

Industry/Entity Type

Store

Requirements
Nice to have
• It should include (if possible) the 2 pics I attached of women with keys in their hands. I don't mind seeing designs without them but hopefully it will help with the "mood" of the design.

```html
<!DOCTYPE html>
<html lang="en">
<head>
<meta charset="utf-8">
<title>Bayside Auto Ally Postcard</title>
<link rel="stylesheet" href="https://fonts.googleapis.com/css2?family=Montserrat:wght@500;600;700&family=Lilita+One&family=Anton&family=Oswald:wght@700&family=Lato:ital,wght@1,900&display=swap">
<style>
  :root {
    --ink: #141414;
    --paper: #ffffff;
    --orange: #f4561c;
    --lime: #80fa0a;
    --sky-top: #b9dff3;
    --sky-mid: #def0fa;
    --window-grey: #8e969e;
    --car-silver: #dfe3e7;
    --car-white: #f6f7f8;
  }
  * { margin: 0; padding: 0; box-sizing: border-box; }
  html, body { width: 1200px; height: 930px; overflow: hidden; background: var(--paper); }
  .postcard { position: relative; width: 1200px; height: 930px; background: var(--paper); overflow: hidden; }

  .brand-name {
    position: absolute; left: 72px; top: 124px; width: 1090px;
    text-align: center;
    font-family: "Montserrat", sans-serif; font-weight: 500;
    font-size: 100px; line-height: 1;
    color: var(--ink); white-space: nowrap;
  }
  .brand-rule {
    position: absolute; left: 72px; top: 243px; width: 1083px; height: 2px;
    background: var(--ink);
  }
  .tagline {
    position: absolute; left: 75px; top: 264px; width: 1065px;
    display: flex; justify-content: space-between;
    font-family: "Montserrat", sans-serif; font-weight: 500;
    font-size: 22px; line-height: 1; color: var(--ink);
  }

  .hero-photo {
    position: absolute; left: 440px; top: 290px; width: 760px; height: 445px;
    background:
      linear-gradient(90deg, var(--paper) 0%, rgba(255,255,255,0) 14%),
      radial-gradient(ellipse 38% 30% at 72% 48%, rgba(120,90,70,0.35) 0%, rgba(120,90,70,0) 100%),
      linear-gradient(180deg, var(--sky-top) 0%, var(--sky-mid) 22%, var(--car-silver) 34%, var(--window-grey) 48%, var(--window-grey) 58%, var(--car-silver) 68%, var(--car-white) 85%, var(--paper) 100%);
  }

  .headline { position: absolute; font-family: "Lilita One", sans-serif; color: var(--ink); line-height: 1; white-space: nowrap; }
  .headline-top { left: 45px; top: 314px; font-size: 62px; letter-spacing: 4px; }
  .headline-overpay { left: 165px; top: 368px; font-family: "Montserrat", sans-serif; font-weight: 600; font-size: 68px; color: var(--orange); }
  .headline-car { left: 178px; top: 440px; font-size: 62px; letter-spacing: 3px; }
  .service-name { position: absolute; left: 45px; top: 516px; font-family: "Oswald", sans-serif; font-weight: 700; font-size: 62px; line-height: 1; color: var(--orange); white-space: nowrap; letter-spacing: 1px; }
  .helps-line { position: absolute; left: 165px; top: 582px; font-family: "Lato", sans-serif; font-style: italic; font-weight: 900; font-size: 46px; line-height: 1; color: var(--ink); white-space: nowrap; }
  .great-deal { position: absolute; left: 40px; top: 626px; font-family: "Anton", sans-serif; font-size: 102px; line-height: 1; color: var(--orange); white-space: nowrap; letter-spacing: 3px; transform-origin: left top; transform: skewX(-12deg) scaleX(1.25); }

  .footer-band {
    position: absolute; left: 0; top: 735px; width: 1200px; height: 195px;
    background: var(--lime);
  }
  .footer-copy {
    position: absolute; left: 330px; top: 752px; width: 600px;
    text-align: center;
    font-family: "Montserrat", sans-serif; font-weight: 700;
    font-size: 22px; line-height: 1.2; color: var(--ink);
  }
  .website {
    position: absolute; left: 0; top: 820px; width: 1200px;
    text-align: center;
    font-family: "Montserrat", sans-serif; font-weight: 700;
    font-size: 42px; line-height: 1; letter-spacing: 0.27em;
    color: var(--paper); white-space: nowrap;
  }
</style>
</head>
<body>
<main class="postcard">
  <div class="brand-name">BAYSIDE AUTO ALLY</div>
  <div class="brand-rule"></div>
  <div class="tagline">
    <span>W</span><span>E</span><span>L</span><span>C</span><span>O</span><span>M</span><span>E</span><span>&nbsp;</span><span>T</span><span>O</span><span>&nbsp;</span><span>S</span><span>M</span><span>A</span><span>R</span><span>T</span><span>&nbsp;</span><span>C</span><span>A</span><span>R</span><span>&nbsp;</span><span>B</span><span>U</span><span>Y</span><span>I</span><span>N</span><span>G</span>
  </div>

  <div class="hero-photo" role="img" aria-label="Photo of a smiling young woman leaning out of a silver car window, holding up a car key, under a bright blue sky"></div>

  <div class="headline headline-top">NO ONE WANTS TO</div>
  <div class="headline headline-overpay">OVERPAY</div>
  <div class="headline headline-car">FOR A CAR</div>
  <div class="service-name">BAYSIDE AUTO ALLY</div>
  <div class="helps-line">helps you get a</div>
  <div class="great-deal">GREAT DEAL</div>

  <div class="footer-band"></div>
  <p class="footer-copy">For Know More About The Benefits Of<br>Car Buying Service, Visit Out Website At</p>
  <div class="website">WWW.BAYSIDEAUTOALLY.COM</div>
</main>
</body>
</html>
```